Freelance Translator in Need of a Business Card

I am a freelance Japanese to English translator. I work in the video game localization industry and do literary translation in my spare time. I would like to have both the English word 'Translator' and the Japanese '翻訳者' in the job title. The final design should evoke trust, openness, and reliability.

Target Market(s)

Video game localization companies
Japanese comic book artists

Industry/Entity Type

Business

Contact Information for Business Card

Daniel Oskerby, Translator
dan.oskerby@fernlowmail.com
velmotranslates.com
social: @velmo_tl

Colors

Designer to choose colors to be used in the design.

```html
<!DOCTYPE html>
<html lang="en">
<head>
<meta charset="utf-8">
<title>Velmo Translates – Business Card</title>
<link rel="stylesheet" href="https://fonts.googleapis.com/css2?family=Raleway:wght@400&family=Lato:wght@300;400&family=Noto+Sans+JP:wght@400&display=swap">
<style>
  :root {
    --page-bg: #2b2b2b;
    --card-bg: #1c1c1c;
    --card-edge: #262626;
    --text-main: #e6e6e6;
    --text-soft: #8a8a8a;
    --rule: #6a6a6a;
    --band-light: #5e5e5e;
    --band-dark: #3a3a3a;
    --icon: #9a9a9a;
  }
  * { margin: 0; padding: 0; box-sizing: border-box; }
  html, body { width: 1200px; height: 900px; overflow: hidden; background: var(--page-bg); }
  .stage { position: relative; width: 1200px; height: 900px; }
  .card {
    position: absolute; left: 330px; width: 540px; height: 309px;
    background: linear-gradient(160deg, var(--card-edge), var(--card-bg) 55%);
    border-radius: 22px; overflow: hidden;
    box-shadow: 0 12px 30px rgba(0,0,0,.45);
  }
  .card--front { top: 110px; }
  .card--back { top: 470px; }
  .wordmark {
    font-family: "Raleway", sans-serif; font-weight: 400;
    color: var(--text-main); letter-spacing: .5px; white-space: nowrap;
  }
  .card--front .brand {
    position: absolute; left: 0; right: 0; top: 118px; text-align: center;
  }
  .card--front .wordmark { font-size: 40px; display: block; line-height: 1; }
  .card--front .brand-url {
    display: block; margin: 6px 0 0 150px;
    font-family: "Raleway", sans-serif; font-size: 14px; color: var(--text-soft);
  }
  .card--back .wordmark { position: absolute; right: 34px; top: 32px; font-size: 34px; }
  .person { position: absolute; left: 44px; top: 108px; }
  .person-name {
    font-family: "Lato", sans-serif; font-weight: 400; font-size: 27px; color: var(--text-main);
    white-space: nowrap;
  }
  .person-role {
    margin-top: 2px; font-family: "Lato", sans-serif; font-weight: 300; font-size: 15px;
    color: var(--text-soft); display: flex; gap: 22px;
  }
  .person-role .ja { font-family: "Noto Sans JP", sans-serif; }
  .divider { margin-top: 18px; width: 150px; height: 2px; background: var(--rule); }
  .contacts { position: absolute; left: 44px; top: 212px; list-style: none; }
  .contacts li {
    display: flex; align-items: center; gap: 12px; height: 24px; white-space: nowrap;
    font-family: "Lato", sans-serif; font-weight: 300; font-size: 15px; color: var(--text-main);
  }
  .contacts svg { width: 16px; height: 16px; flex: none; }
  .band { position: absolute; bottom: 0; height: 12px; }
  .band--light { left: 250px; right: 0; background: var(--band-light); }
  .band--dark { right: 0; width: 100px; bottom: 12px; height: 8px; background: var(--band-dark); }
</style>
</head>
<body>
<main class="stage">
  <section class="card card--front" aria-label="Card front">
    <div class="brand">
      <span class="wordmark">Velmo Translates</span>
      <span class="brand-url">velmotranslates.com</span>
    </div>
  </section>

  <section class="card card--back" aria-label="Card back">
    <span class="wordmark">Velmo Translates</span>
    <div class="person">
      <h1 class="person-name">Daniel Oskerby</h1>
      <p class="person-role"><span>Translator</span><span class="ja">翻訳者</span></p>
      <div class="divider"></div>
    </div>
    <ul class="contacts">
      <li>
        <svg viewBox="0 0 16 16" aria-hidden="true"><rect x="1.5" y="3.5" width="13" height="9" fill="none" stroke="var(--icon)" stroke-width="1.4"/><path d="M1.5 3.5 8 9l6.5-5.5" fill="none" stroke="var(--icon)" stroke-width="1.4"/></svg>
        dan.oskerby@fernlowmail.com
      </li>
      <li>
        <svg viewBox="0 0 16 16" aria-hidden="true"><circle cx="8" cy="8" r="6.5" fill="none" stroke="var(--icon)" stroke-width="1.3"/><ellipse cx="8" cy="8" rx="3" ry="6.5" fill="none" stroke="var(--icon)" stroke-width="1.1"/><path d="M1.5 8h13" stroke="var(--icon)" stroke-width="1.1"/></svg>
        velmotranslates.com
      </li>
      <li>
        <svg viewBox="0 0 16 16" aria-hidden="true"><circle cx="8" cy="8" r="5.5" fill="var(--icon)"/></svg>
        social: @velmo_tl
      </li>
    </ul>
    <div class="band band--dark"></div>
    <div class="band band--light"></div>
  </section>
</main>
</body>
</html>
```